Web Design Project

This web site is to be designed for a popular Cambodian singer, Vanny Kolthida. Web site name "Vanny Kolthida".

The purpose is to keep her fans update with the latest of her entertainment career and invite them to help raising fund for Lotus Bridge Youth Fund.

In addition to other normal pages such as HOME, ABOUT... This web site must be:
1. able to link to Dropshipers and add Products
2. able to donate (accept Major Credit Cards or PayVira)
3. able to purchase products (accept Major Credit Cards or PayVira)
4. able to video live chat with Vanny Kolthida
5. able to book appointment on her calendar

Here is a sample of the web site:
http://pralay82.sitebuildo.example/vanny-kol-thida

Please call me if you need any clarification at 1-555-281-3097 or leave your number for me to call you back.

Thank you

Dara

Target Market(s)

Cambodian living abroad

Industry/Entity Type

Entertainment

Requirements
Must have
• 1. able to link to Dropshipers and add Products
2. able to Donate (accept Major Credit Cards or PayVira)

```html
<!DOCTYPE html>
<html lang="en">
<head>
<meta charset="utf-8">
<title>Vanny Kolthida</title>
<link href="https://fonts.googleapis.com/css2?family=Arimo:ital,wght@0,400;0,700;1,400&family=Open+Sans:wght@400;700&family=PT+Sans+Narrow:wght@400;700&family=Ubuntu:wght@700&family=Yanone+Kaffeesatz:wght@300;400&display=swap" rel="stylesheet">
<style>
:root{
  --bg:#0b0708;
  --ink:#ffffff;
  --muted:#b9b4b2;
  --rule:#4a4544;
  --accent:#f08a2c;
  --orange:#e8650f;
}
*{margin:0;padding:0;box-sizing:border-box}
html,body{width:1006px;height:1200px;overflow:hidden;background:var(--bg)}
.page{position:relative;width:1006px;height:1200px;overflow:hidden;
  background:
    radial-gradient(ellipse 520px 240px at 520px 10px,#5a2a7a 0%,rgba(60,20,80,0) 70%),
    radial-gradient(ellipse 700px 420px at 500px 700px,#3a1410 0%,rgba(30,10,8,0) 75%),
    linear-gradient(#1f0f2a 0,#2a0e26 300px,#1a0a0c 560px,var(--bg) 1060px);
  font-family:Arimo,Arial,sans-serif;color:var(--ink)}
.abs{position:absolute}
.logo{left:104px;top:24px;font-family:Ubuntu,sans-serif;font-weight:700;font-size:28px;letter-spacing:.5px;color:#d8d6d6}
.nav{top:34px;font-size:11.5px;color:var(--ink);letter-spacing:.3px}
.nav-pill{left:525px;top:32px;width:60px;height:19px;border-radius:10px;background:linear-gradient(#e9e9e9,#a9a9a9);color:#222;text-align:center;line-height:19px;font-size:11.5px}
.head-rule{left:70px;top:64px;width:900px;height:1px;background:linear-gradient(90deg,rgba(120,120,140,0),#6d6a7a 20%,#6d6a7a 80%,rgba(120,120,140,0))}
.hero-frame{left:91px;top:92px;width:824px;height:400px;background:linear-gradient(#4b4e52,#24272a);border:1px solid #5a5d60}
.hero-inner{left:103px;top:102px;width:800px;height:390px;background:#000}
.hero-photo{left:128px;top:123px;width:752px;height:360px;border-top:3px solid #3a3a3a;
  background:linear-gradient(100deg,#120a0e 0%,#1c0f16 35%,#3a2030 60%,#2a1420 78%,#100a0c 100%)}
.band{left:0;top:482px;width:1006px;height:94px;background:linear-gradient(#2a333b,#1c232a);border-top:1px solid #55606a;border-bottom:1px solid #0d1014}
.band-notch{left:492px;top:471px}
.thumb-track{left:120px;top:488px;width:766px;height:82px;background:linear-gradient(#3c4147,#8b9095 50%,#3c4147);opacity:.7}
.thumb{top:494px;width:134px;height:69px;border:2px solid #c9c9c9}
.arrow{top:517px;width:26px;height:27px;background:linear-gradient(#8b8f93,#55595d)}
.arrow.left{left:95px;border-radius:13px 0 0 13px}
.arrow.right{left:885px;border-radius:0 13px 13px 0}
.h2{font-family:"Yanone Kaffeesatz",sans-serif;font-weight:300;font-size:26px;font-style:italic;color:var(--ink);line-height:1}
.rule{height:1px;background:var(--rule)}
.pic{width:98px;height:98px;border:2px solid #e07a3a}
.title{font-family:"Yanone Kaffeesatz",sans-serif;font-weight:400;font-size:22px;color:var(--accent);line-height:1}
.body{font-size:10.6px;line-height:17.6px;color:var(--muted)}
.purpose{font-family:"Open Sans",sans-serif;font-size:13.4px;line-height:18.5px;color:#d6d2d0}
.purpose b{color:#fff}
.tick{display:inline-block;vertical-align:-1px;margin-right:5px}
.link{color:var(--accent);font-style:italic}
.about{font-style:italic;font-size:10.6px;line-height:17px;color:var(--muted)}
.help{font-family:"Yanone Kaffeesatz",sans-serif;font-size:17px;color:#c9c5c3}
.charity{font-family:"Yanone Kaffeesatz",sans-serif;font-size:23px;color:#d9d6d4}
.field{left:659px;top:868px;width:168px;height:18px;background:#fff;border:1px solid #9a9a9a;font-size:9px;color:#333;padding:4px 6px}
.btn{left:839px;top:868px;width:73px;height:18px;background:var(--orange);font-size:10px;font-weight:700;text-align:center;line-height:18px}
.merch{width:57px;height:45px;border:1px solid #8a8a8a}
.footer{left:0;top:1068px;width:1006px;height:70px;background:#101214;border-top:3px solid #3a3d40}
.footer2{left:0;top:1138px;width:1006px;height:62px;background:linear-gradient(#25282b,#161819);border-top:3px solid #3d4043}
.brand{font-family:Arimo,sans-serif;font-size:21px;color:#d9d9d9}
.social{top:1085px;width:48px;height:40px;background:linear-gradient(#5a5e62,#2b2e31);border:1px solid #6a6e72;border-radius:3px;font-size:8px;font-weight:700;color:#e5e5e5;text-align:center;line-height:38px;white-space:nowrap;overflow:hidden}
.fnav{top:1153px;font-family:"PT Sans Narrow",sans-serif;font-weight:700;font-size:11.5px;color:#c4c4c4}
.copy{left:0;top:1176px;width:1006px;text-align:center;font-family:"PT Sans Narrow",sans-serif;font-weight:700;font-size:11.5px;color:#b4b4b4}
</style>
</head>
<body>
<div class="page">
  <header>
    <div class="abs logo">VANNY KOLTHIDA</div>
    <nav>
      <div class="abs nav-pill">HOME</div>
      <div class="abs nav" style="left:647px">ABOUT</div>
      <div class="abs nav" style="left:752px">STORE</div>
      <div class="abs nav" style="left:852px">LIVE CHAT</div>
    </nav>
    <div class="abs head-rule"></div>
  </header>

  <section class="hero">
    <div class="abs hero-frame"></div>
    <div class="abs hero-inner"></div>
    <div class="abs hero-photo" role="img" aria-label="Stage photo of the singer performing under coloured lights"></div>
    <div class="abs band"></div>
    <div class="abs thumb-track"></div>
    <svg class="abs band-notch" width="22" height="12" viewBox="0 0 22 12"><path d="M0 12 L11 0 L22 12Z" fill="#6c7277"/></svg>
    <div class="abs arrow left"><svg width="26" height="27"><path d="M16 8 L11 13.5 L16 19" stroke="#e87a2a" stroke-width="2.5" fill="none"/></svg></div>
    <div class="abs thumb" style="left:128px;background:linear-gradient(110deg,#3a1e4a,#2d4fb0 55%,#d4b22a)" role="img" aria-label="Concert stage thumbnail"></div>
    <div class="abs thumb" style="left:282px;background:linear-gradient(90deg,#8a4a3a,#4a2a24 45%,#e05a2a)" role="img" aria-label="Singing with microphone thumbnail"></div>
    <div class="abs thumb" style="left:437px;background:linear-gradient(90deg,#1a0c10,#7a4a44 60%,#241414)" role="img" aria-label="Close-up performance thumbnail"></div>
    <div class="abs thumb" style="left:591px;background:linear-gradient(90deg,#3a3a2a,#6a6a4a 45%,#2a2a24)" role="img" aria-label="Duet on stage thumbnail"></div>
    <div class="abs thumb" style="left:743px;background:linear-gradient(110deg,#9a3ac0,#c05ad0 50%,#6a2a8a)" role="img" aria-label="Portrait with parasol thumbnail"></div>
    <div class="abs arrow right"><svg width="26" height="27"><path d="M10 8 L15 13.5 L10 19" stroke="#2a2c2e" stroke-width="2.5" fill="none"/></svg></div>
  </section>

  <main>
    <section>
      <h2 class="abs h2" style="left:95px;top:600px">Store</h2>
      <div class="abs rule" style="left:95px;top:629px;width:538px"></div>
      <div class="abs pic" style="left:95px;top:640px;background:linear-gradient(#f2eeee,#d8cfcf)" role="img" aria-label="Product promo photo of the singer"></div>
      <h3 class="abs title" style="left:210px;top:643px">Purchase Products</h3>
      <p class="abs body" style="left:210px;top:669px;width:420px">Lorem Ipsum is simply dummy text of the printing and typesetting industry. Lorem Ipsum has been the industry's standard dummy text ever since the 1500s, when an unknown printer took a galley of type and scrambled it to make a type specimen book. It has survived not only five centuries, but also the leap into electronic typesetting.</p>
    </section>

    <section>
      <h2 class="abs h2" style="left:95px;top:750px">Purpose</h2>
      <div class="abs rule" style="left:95px;top:780px;width:538px"></div>
      <div class="abs pic" style="left:95px;top:792px;background:linear-gradient(#b8c8da,#5a2020 75%,#c02020)" role="img" aria-label="Portrait of the singer in a graphic tee"></div>
      <h3 class="abs title" style="left:210px;top:793px">Why This Site?</h3>
      <p class="abs purpose" style="left:210px;top:818px;width:425px"><svg class="tick" width="11" height="10"><path d="M1 5 L4 8.5 L10 1" stroke="#e8e8e8" stroke-width="1.8" fill="none"/></svg>I would like to keep you all update with the latest of my entertainment career.</p>
      <p class="abs purpose" style="left:210px;top:859px;width:425px"><svg class="tick" width="11" height="10"><path d="M1 5 L4 8.5 L10 1" stroke="#e8e8e8" stroke-width="1.8" fill="none"/></svg>Another purpose of this site is to help raising fund for <b>Lotus Bridge Youth Fund.</b></p>
    </section>

    <section>
      <h2 class="abs h2" style="left:95px;top:902px">Live Chat</h2>
      <div class="abs rule" style="left:95px;top:931px;width:538px"></div>
      <div class="abs pic" style="left:95px;top:942px;background:linear-gradient(120deg,#6a5040,#2a1a14 55%,#a08070)" role="img" aria-label="Candid photo of the singer laughing"></div>
      <h3 class="abs title" style="left:210px;top:946px">You Can Talk To Vanny Kolthida</h3>
      <p class="abs body" style="left:210px;top:973px;width:426px">Lorem Ipsum is simply dummy text of the printing and typesetting industry. Lorem Ipsum has been the industry's standard dummy text ever since the 1500s, when an unknown printer took a galley of type and scrambled it to make a type specimen book. It has survived not only five centuries......... <span class="link">Click Here</span></p>
    </section>

    <aside>
      <h2 class="abs h2" style="left:659px;top:600px">About Me</h2>
      <div class="abs rule" style="left:659px;top:629px;width:254px"></div>
      <p class="abs about" style="left:659px;top:642px;width:256px">"Lorem ipsum dolor sit amet, consectetur adipisicing elit, sed do eiusmod tempor incididunt ut labore et dolore magna aliqua. Ut enim ad minim veniam, quis nostrud exercitation ullamco laboris nisi ut aliquip ex ea commodo consequat. Duis aute irure dolor in reprehenderit in voluptate velit esse cillum dolore eu fugiat nulla pariatur"</p>

      <h2 class="abs h2" style="left:659px;top:775px">Donate</h2>
      <div class="abs rule" style="left:659px;top:804px;width:254px"></div>
      <div class="abs" style="left:655px;top:820px;width:46px;height:32px;background:radial-gradient(ellipse at 50% 80%,#8a8a8a,rgba(60,60,60,0) 70%)" role="img" aria-label="Icon of people"></div>
      <div class="abs help" style="left:709px;top:815px">Help us raise funds for</div>
      <div class="abs charity" style="left:709px;top:832px">Lotus Bridge Youth Fund</div>
      <div class="abs field">Email Address</div>
      <div class="abs btn">DONATE</div>

      <h2 class="abs h2" style="left:659px;top:908px">Shop Merchandise</h2>
      <div class="abs rule" style="left:659px;top:937px;width:254px"></div>
      <div class="abs merch" style="left:661px;top:947px;background:linear-gradient(#2a2a2a,#c8a060 60%,#1a1a1a)" role="img" aria-label="Black printed tee"></div>
      <div class="abs merch" style="left:727px;top:947px;background:linear-gradient(#d8c8c0,#c02a2a 50%)" role="img" aria-label="Red tee"></div>
      <div class="abs merch" style="left:792px;top:947px;background:linear-gradient(#d8d0c0,#f0f0f0 50%)" role="img" aria-label="White printed tee"></div>
      <div class="abs merch" style="left:856px;top:947px;background:linear-gradient(#5a4038,#1a1a1a 55%)" role="img" aria-label="Black fitted tee"></div>
      <div class="abs merch" style="left:661px;top:1006px;background:linear-gradient(#c89a98,#9a6a68)" role="img" aria-label="Pink tee"></div>
      <div class="abs merch" style="left:727px;top:1006px;background:linear-gradient(#e8e8ee,#ffffff)" role="img" aria-label="White tee"></div>
      <div class="abs merch" style="left:792px;top:1006px;background:linear-gradient(#c0c8d0,#1a2a4a 50%)" role="img" aria-label="Navy printed tee"></div>
      <div class="abs merch" style="left:856px;top:1006px;background:linear-gradient(#d8e0c8,#6ab04a 50%)" role="img" aria-label="Green tee"></div>
    </aside>
  </main>

  <footer>
    <div class="abs footer"></div>
    <div class="abs brand" style="left:96px;top:1090px">Chirpline</div>
    <p class="abs body" style="left:192px;top:1088px;width:380px;color:#cfcfcf">Lorem ipsum dolor sit amet, consectetur adipisicing elit, sed do eiusmod tempor incididunt ut labore et dolore magna aliqua. Ut enim ad minim veniam.</p>
    <div class="abs" style="left:641px;top:1082px;width:1px;height:44px;background:#3e4145"></div>
    <div class="abs social" style="left:690px">Friendloop</div>
    <div class="abs social" style="left:745px">Pickpile</div>
    <div class="abs social" style="left:800px">Feed</div>
    <div class="abs social" style="left:855px">Snapgrove</div>
    <div class="abs footer2"></div>
    <div class="abs fnav" style="left:300px">HOME</div>
    <div class="abs fnav" style="left:356px">|</div>
    <div class="abs fnav" style="left:388px">ABOUT</div>
    <div class="abs fnav" style="left:456px">|</div>
    <div class="abs fnav" style="left:487px">VIDEO</div>
    <div class="abs fnav" style="left:544px">|</div>
    <div class="abs fnav" style="left:571px">STORE</div>
    <div class="abs fnav" style="left:626px">|</div>
    <div class="abs fnav" style="left:653px">LIVE CHAT</div>
    <div class="abs copy">Copyright © Vanny Kolthida</div>
  </footer>
</div>
</body>
</html>
```